JesterVolt Balloon Logo and Product Packaging Design

I need a package design for twisting balloons for my website jestervoltfun.com. The brand name that we will use is "jestervolt". The packaging will be 40cm long x 15 cm width with a see thru front and a top that can tear off. We can only use 3 colors max, but two colors would be better. We also will need a logo for "jestervolt". I have included our mockup front and back, our competitors packaging and our style guide. You can use our style guide and our mockups for inspiration but you please don't follow it exactly. You can also ignore them all together. Thanks, Corin

```html
<!DOCTYPE html>
<html lang="en">
<head>
<meta charset="utf-8">
<title>JesterVolt Twisting Balloons Package</title>
<link rel="stylesheet" href="https://fonts.googleapis.com/css2?family=Lilita+One&family=Oswald:wght@600&family=Rubik:wght@400&display=swap">
<style>
  :root {
    --page: #ffffff;
    --yellow: #fbf906;
    --coral: #f64953;
    --warning-red: #ff0000;
    --sky: #27a8e8;
    --ink: #222222;
    --white: #ffffff;
    --hanger: #3a3a3a;
    --green-dark: #1f8a45;
    --green-mid: #2fa657;
    --green-light: #4cbf7a;
  }
  html, body {
    margin: 0;
    padding: 0;
    width: 1200px;
    height: 2934px;
    overflow: hidden;
    background: var(--page);
  }
  .package {
    display: block;
    width: 1200px;
    height: 2934px;
  }
  .brand-name { font-family: "Lilita One", sans-serif; fill: var(--coral); }
  .badge-high { font-family: "Lilita One", sans-serif; fill: var(--sky); }
  .badge-party { font-family: "Lilita One", sans-serif; fill: var(--coral); }
  .warning-title { font-family: "Oswald", sans-serif; font-weight: 600; fill: var(--white); }
  .warning-copy { font-family: "Rubik", sans-serif; fill: var(--ink); }
  .count, .footer-brand { font-family: "Lilita One", sans-serif; fill: var(--white); }
</style>
</head>
<body>
<svg class="package" viewBox="0 0 1050 2567.5" xmlns="http://www.w3.org/2000/svg">
  <defs>
    <linearGradient id="window-tone" x1="0" y1="0" x2="1" y2="0">
      <stop offset="0" stop-color="var(--green-dark)"/>
      <stop offset="0.35" stop-color="var(--green-mid)"/>
      <stop offset="0.6" stop-color="var(--green-dark)"/>
      <stop offset="0.85" stop-color="var(--green-light)"/>
      <stop offset="1" stop-color="var(--green-mid)"/>
    </linearGradient>
  </defs>

  <!-- card body -->
  <rect class="card" x="96" y="140" width="862" height="2297" fill="var(--yellow)"/>

  <!-- hang tab -->
  <g class="hang-hole" fill="var(--hanger)">
    <circle cx="558" cy="178" r="22"/>
    <rect x="418" y="183" width="282" height="37" rx="18.5"/>
  </g>

  <!-- brand name -->
  <text class="brand-name" x="527" y="535" text-anchor="middle" font-size="112" textLength="740" lengthAdjust="spacingAndGlyphs">JESTERVOLT</text>

  <!-- balloon animal illustration area -->
  <g class="balloon-art" role="img" aria-label="Twisted balloon dog and giraffes">
    <ellipse cx="810" cy="395" rx="105" ry="52" fill="var(--coral)" opacity="0.35"/>
  </g>

  <!-- see-through window -->
  <path class="window" role="img" aria-label="Green twisting balloons seen through the clear window"
        d="M96,950 C250,880 450,860 520,800 C560,760 580,720 640,710 C720,700 760,730 830,720 C900,710 930,620 958,580 L958,1857 L96,1857 Z"
        fill="url(#window-tone)"/>

  <!-- coral wave above window -->
  <path class="window-edge" fill="var(--coral)"
        d="M96,895 C250,825 450,805 505,740 C545,690 580,665 640,660 C720,655 760,690 830,680 C890,670 920,560 958,535 L958,580 C930,620 900,710 830,720 C760,730 720,700 640,710 C580,720 560,760 520,800 C450,860 250,880 96,950 Z"/>

  <!-- quality badge -->
  <g class="quality-badge">
    <g fill="var(--coral)">
      <circle cx="316" cy="765" r="100"/>
      <circle cx="420" cy="860" r="100"/>
      <circle cx="316" cy="975" r="105"/>
      <circle cx="215" cy="870" r="100"/>
      <circle cx="390" cy="950" r="85"/>
      <circle cx="240" cy="950" r="85"/>
      <circle cx="240" cy="785" r="80"/>
      <circle cx="395" cy="785" r="80"/>
    </g>
    <g fill="var(--white)">
      <circle cx="316" cy="770" r="78"/>
      <circle cx="400" cy="860" r="80"/>
      <circle cx="316" cy="965" r="85"/>
      <circle cx="228" cy="870" r="80"/>
      <circle cx="378" cy="940" r="68"/>
      <circle cx="252" cy="940" r="68"/>
      <circle cx="250" cy="795" r="62"/>
      <circle cx="385" cy="795" r="62"/>
      <circle cx="316" cy="870" r="110"/>
    </g>
    <text class="badge-high" x="318" y="830" text-anchor="middle" font-size="76">HIGH</text>
    <text class="badge-high" x="318" y="890" text-anchor="middle" font-size="66">QUALITY</text>
    <text class="badge-party" x="315" y="951" text-anchor="middle" font-size="46">PARTY</text>
    <text class="badge-party" x="315" y="995" text-anchor="middle" font-size="46">BALLOONS</text>
  </g>

  <!-- warning band -->
  <rect class="warning-band" x="96" y="1857" width="862" height="88" fill="var(--warning-red)"/>
  <g class="warning-icon">
    <path d="M174,1873 L201,1920 L147,1920 Z" fill="var(--white)"/>
    <rect x="171" y="1886" width="6" height="19" fill="var(--warning-red)"/>
    <rect x="171" y="1909" width="6" height="6" fill="var(--warning-red)"/>
  </g>
  <text class="warning-title" x="215" y="1930" font-size="62" textLength="695" lengthAdjust="spacingAndGlyphs">WARNING : CHOKING HAZARD</text>

  <g class="warning-copy" font-size="27" text-anchor="middle">
    <text x="530" y="1995">Children under eight (8) years old can choke or suffocate</text>
    <text x="527" y="2032">on uninflated or broken balloons. adult supervision is</text>
    <text x="527" y="2068">required. keep uninflated balloons from reach of children.</text>
    <text x="527" y="2105">discard broken balloons responsibly.</text>
  </g>

  <!-- bottom waves -->
  <path class="footer-stripe" fill="var(--coral)"
        d="M96,2120 C250,2105 330,2160 440,2150 C560,2140 620,2105 740,2110 C850,2115 900,2140 958,2160 L958,2195 C900,2175 850,2150 740,2145 C620,2140 560,2180 440,2188 C330,2196 250,2140 96,2155 Z"/>
  <path class="footer-band" fill="var(--coral)"
        d="M96,2175 C250,2160 330,2220 450,2215 C570,2210 630,2165 750,2168 C860,2171 910,2195 958,2215 L958,2437 L96,2437 Z"/>

  <text class="count" x="145" y="2337" font-size="88">100<tspan font-size="48">Pcs</tspan></text>
  <text class="footer-brand" x="475" y="2335" font-size="72" textLength="450" lengthAdjust="spacingAndGlyphs">JESTERVOLT</text>
</svg>
</body>
</html>
```